Psychotherapist's business card

I need a business card design for a psychotherapist. I expect business card to have "light" design. By this I mean that it can somehow translate easiness, serenity. Maybe pastel colours can help you here. I have attached some pictures from Greece. Perhaps they can inspire you to combine colours and to achieve that "light" design.
Updates

Pls, don't use any free samples you may find on business card generators. It looks too simple, uncreative and waste of time! READ size and colour requirements! I don't want to see any shapes like rings, triangles etc.

Contact Information for Business Card

Size: 65mmX60mm

Name - Вячеслав Мирошенко

Психолог
+7(916)482-30-67
miroshenko.com

I suppose that thin font can look good but it's up to you

Requirements
Must have
• size requirements
Nice to have
• pastel colours
• thin font
Should not have
• black and dark colours
• lines, free design samples used from other web-sites

```html
<!DOCTYPE html>
<html lang="ru">
<head>
<meta charset="utf-8">
<title>Визитка психолога — Вячеслав Мирошенко</title>
<link rel="stylesheet" href="https://fonts.googleapis.com/css2?family=Jura:wght@300;400&display=swap">
<style>
  :root {
    --backdrop: #dedede;
    --teal: #3fa9a3;
    --gold: #c9a03a;
    --gold-wash: rgba(214, 178, 92, 0.55);
    --paper: #f4f4f2;
    --ink: #6a6a6a;
    --white: #ffffff;
  }
  html, body {
    margin: 0;
    padding: 0;
    width: 1200px;
    height: 748px;
    overflow: hidden;
    background: var(--backdrop);
    font-family: "Jura", sans-serif;
  }
  .canvas {
    position: relative;
    width: 1200px;
    height: 748px;
  }
  /* 65 × 60 mm at 5 px/mm */
  .card {
    position: absolute;
    top: 224px;
    width: 325px;
    height: 300px;
    box-sizing: border-box;
    overflow: hidden;
  }
  .card--front {
    left: 240px;
    background: var(--teal);
  }
  .card--back {
    left: 635px;
    background: var(--paper);
  }
  .front-glow {
    position: absolute;
    inset: 0;
    background: radial-gradient(circle at 100% 0%, var(--gold-wash) 0%, rgba(214, 178, 92, 0) 55%);
  }
  .front-name {
    position: absolute;
    left: 30px;
    bottom: 34px;
    margin: 0;
    color: var(--white);
    font-weight: 300;
    font-size: 23px;
    line-height: 1.15;
    letter-spacing: 0.5px;
    text-transform: uppercase;
  }
  .back-content {
    position: absolute;
    left: 70px;
    top: 78px;
    right: 24px;
  }
  .back-name {
    margin: 0;
    color: var(--ink);
    font-weight: 400;
    font-size: 19px;
    line-height: 1.15;
    letter-spacing: 0.4px;
    text-transform: uppercase;
  }
  .back-role {
    margin: 10px 0 0 48px;
    color: var(--teal);
    font-size: 14px;
    font-weight: 400;
  }
  .back-contacts {
    margin: 20px 0 0 48px;
    padding: 0;
    list-style: none;
    color: var(--ink);
    font-size: 13px;
    line-height: 1.35;
    letter-spacing: 0.3px;
    text-transform: uppercase;
    white-space: nowrap;
  }
</style>
</head>
<body>
  <main class="canvas">
    <section class="card card--front" aria-label="Лицевая сторона визитки">
      <div class="front-glow" aria-hidden="true"></div>
      <h1 class="front-name">Вячеслав<br>Мирошенко</h1>
    </section>

    <section class="card card--back" aria-label="Оборотная сторона визитки">
      <div class="back-content">
        <h2 class="back-name">Вячеслав<br>Мирошенко</h2>
        <p class="back-role">психолог</p>
        <ul class="back-contacts">
          <li>+7(916)482-30-67</li>
          <li>psymirosh@mirpost.ru</li>
          <li>miroshenko.com</li>
        </ul>
      </div>
    </section>
  </main>
</body>
</html>
```